Gift box company needs packaging design for shipping box

We need a design to decorate our brown cardboard shipping boxes. The design must include our company logo (provided) and a "fragile" label somewhere. We will be using single colour printing so the design must only be in one colour. As it will be covering a brown box, I think black or dark blue would be most appropriate. The shipping box itself measures 355mm wide X 246mm deep X 105mm tall. If the design could make the box look like a wrapped present in some way, that would be great.

```html
<!DOCTYPE html>
<html lang="en">
<head>
<meta charset="utf-8">
<title>Kindly Given – Shipping Box Dieline</title>
<link href="https://fonts.googleapis.com/css2?family=Montserrat:wght@600&display=swap" rel="stylesheet">
<style>
  :root {
    --bg-top: #6a6a6a;
    --bg-bottom: #000000;
    --kraft: #c6a384;
    --ink: #111111;
    --fold: #3b2b20;
    --bow-tone: #b8967a;
  }
  html, body {
    margin: 0;
    padding: 0;
    overflow: hidden;
  }
  .canvas {
    width: 1200px;
    height: 646px;
    background: linear-gradient(to bottom, var(--bg-top) 0%, #3a3a3a 35%, var(--bg-bottom) 75%);
    overflow: hidden;
  }
  .dieline {
    display: block;
    width: 1200px;
    height: 646px;
  }
  .panel { fill: var(--kraft); }
  .fold-line { stroke: var(--fold); stroke-width: 1; fill: none; }
  .ribbon-band { fill: var(--ink); }
  .brand-name {
    font-family: "Montserrat", sans-serif;
    font-weight: 600;
    font-size: 30px;
    fill: var(--ink);
    letter-spacing: 1px;
  }
  .bow-area { fill: var(--bow-tone); opacity: 0.55; }
  .fragile-badge { fill: none; stroke: var(--ink); stroke-width: 1.2; }
  .fragile-text {
    font-family: "Montserrat", sans-serif;
    font-weight: 600;
    font-size: 5.5px;
    fill: var(--ink);
  }
  .fragile-arrow { stroke: var(--ink); stroke-width: 1.4; fill: none; }
</style>
</head>
<body>
<div class="canvas">
  <svg class="dieline" viewBox="0 0 1535 826" xmlns="http://www.w3.org/2000/svg">
    <defs>
      <filter id="drop" x="-10%" y="-10%" width="120%" height="130%">
        <feDropShadow dx="0" dy="12" stdDeviation="14" flood-color="#000" flood-opacity="0.6"/>
      </filter>
    </defs>

    <g class="box-net" filter="url(#drop)">
      <path class="panel" d="M68 352 L68 474 L52 468 L47 460 L47 366 L52 356 Z"/>
      <rect class="panel" x="68" y="352" width="420" height="122"/>
      <rect class="panel" x="488" y="352" width="291" height="122"/>
      <path class="panel" d="M488 352 L545 295 L770 295 L779 352 Z"/>
      <path class="panel" d="M488 474 L779 474 L770 531 L545 531 Z"/>
      <path class="panel" d="M779 352 L779 225 Q779 202 805 202 L1172 200 Q1198 200 1198 225 L1198 352 Z"/>
      <rect class="panel" x="779" y="352" width="419" height="122"/>
      <path class="panel" d="M779 474 L1198 474 L1198 600 Q1198 626 1172 625 L805 622 Q779 622 779 598 Z"/>
      <rect class="panel" x="1198" y="352" width="291" height="122"/>
      <path class="panel" d="M1198 352 L1207 295 L1432 295 L1489 352 Z"/>
      <path class="panel" d="M1198 474 L1489 474 L1432 531 L1207 531 Z"/>
    </g>

    <g class="folds">
      <line class="fold-line" x1="68" y1="352" x2="68" y2="474"/>
      <line class="fold-line" x1="47" y1="352" x2="1489" y2="352"/>
      <line class="fold-line" x1="47" y1="474" x2="1489" y2="474"/>
      <line class="fold-line" x1="488" y1="352" x2="488" y2="474"/>
      <line class="fold-line" x1="779" y1="210" x2="779" y2="615"/>
      <line class="fold-line" x1="1198" y1="210" x2="1198" y2="615"/>
      <line class="fold-line" x1="779" y1="228" x2="1198" y2="228"/>
      <line class="fold-line" x1="779" y1="597" x2="1198" y2="597"/>
    </g>

    <g class="ribbon">
      <rect class="ribbon-band" x="68" y="396" width="129" height="34"/>
      <rect class="ribbon-band" x="355" y="396" width="133" height="34"/>
      <rect class="ribbon-band" x="779" y="396" width="128" height="34"/>
      <rect class="ribbon-band" x="1064" y="396" width="134" height="34"/>
    </g>

    <g class="bows">
      <g role="img" aria-label="Faint ribbon bow decoration">
        <ellipse class="bow-area" cx="812" cy="257" rx="30" ry="22"/>
      </g>
      <g role="img" aria-label="Faint ribbon bow decoration">
        <ellipse class="bow-area" cx="1162" cy="316" rx="32" ry="24"/>
      </g>
    </g>

    <g class="brand">
      <text class="brand-name" text-anchor="middle"><tspan x="276" y="412">Kindly</tspan><tspan x="276" y="446">Given</tspan></text>
      <text class="brand-name" text-anchor="middle"><tspan x="986" y="412">Kindly</tspan><tspan x="986" y="446">Given</tspan></text>
      <text class="brand-name" text-anchor="middle" transform="rotate(180 986 300)"><tspan x="986" y="290">Kindly</tspan><tspan x="986" y="324">Given</tspan></text>
    </g>

    <g class="fragile-label" transform="translate(734 423)">
      <rect class="fragile-badge" x="0" y="0" width="32" height="40"/>
      <path class="fragile-arrow" d="M8 6 L8 26 M5 10 L8 6 L11 10 M18 26 L18 8 M15 12 L18 8 L21 12 M24 26 L24 8 M21 12 L24 8 L27 12"/>
      <text class="fragile-text" x="16" y="37" text-anchor="middle">FRAGILE</text>
    </g>
    <g class="fragile-label" transform="translate(1443 423)">
      <rect class="fragile-badge" x="0" y="0" width="32" height="40"/>
      <path class="fragile-arrow" d="M8 6 L8 26 M5 10 L8 6 L11 10 M18 26 L18 8 M15 12 L18 8 L21 12 M24 26 L24 8 M21 12 L24 8 L27 12"/>
      <text class="fragile-text" x="16" y="37" text-anchor="middle">FRAGILE</text>
    </g>
  </svg>
</div>
</body>
</html>
```